KORBALT

The business want a professional looking business card. We have a scetch we will add but want the extra upgrade, and would like more suggestions for variations of our business cards.

```html
<!DOCTYPE html>
<html lang="en">
<head>
<meta charset="utf-8">
<title>KORBALT Business Card</title>
<link rel="stylesheet" href="https://fonts.googleapis.com/css2?family=Montserrat:wght@400;500;600;700&display=swap">
<style>
  :root {
    --page-bg: #ffffff;
    --label-grey: #7a7a7a;
    --gold-dark: #7a5a2a;
    --gold-mid: #a88b4e;
    --gold-light: #cdb16c;
    --gold-pale: #e4d4a8;
    --mark-yellow: #f8e08a;
    --text-light: #f6eed8;
    --icon-light: #efe3c0;
  }
  * { margin: 0; padding: 0; box-sizing: border-box; }
  html, body {
    width: 1200px;
    height: 679px;
    overflow: hidden;
    background: var(--page-bg);
    font-family: "Montserrat", sans-serif;
  }
  .presentation {
    position: relative;
    width: 1200px;
    height: 679px;
  }
  .side-label {
    position: absolute;
    top: 149px;
    width: 426px;
    text-align: center;
    font-size: 19px;
    font-weight: 400;
    letter-spacing: 0.5px;
    color: var(--label-grey);
  }
  .side-label--front { left: 127px; }
  .side-label--back { left: 662px; }

  .card {
    position: absolute;
    top: 209px;
    width: 426px;
    height: 255px;
    overflow: hidden;
    box-shadow: 0 18px 34px rgba(90, 70, 30, 0.22);
  }
  .card--front {
    left: 127px;
    background: linear-gradient(20deg, var(--gold-dark) 0%, var(--gold-mid) 40%, var(--gold-light) 75%, var(--gold-pale) 100%);
  }
  .card--back {
    left: 662px;
    background: linear-gradient(22deg, var(--gold-dark) 0%, var(--gold-mid) 38%, var(--gold-light) 72%, var(--gold-pale) 100%);
  }

  /* front */
  .brand-block {
    position: absolute;
    left: 0;
    top: 56px;
    width: 100%;
    text-align: center;
    color: var(--mark-yellow);
  }
  .brand-dot {
    width: 62px;
    height: 62px;
    margin: 0 auto 22px;
    border-radius: 50%;
    background: var(--mark-yellow);
  }
  .brand-name {
    font-size: 36px;
    font-weight: 500;
    letter-spacing: 3px;
    line-height: 1;
  }
  .brand-since {
    margin-top: 9px;
    font-size: 12px;
    font-weight: 500;
    letter-spacing: 4px;
  }

  /* back */
  .back-brand {
    position: absolute;
    left: 38px;
    top: 80px;
    width: 112px;
    text-align: center;
    color: var(--mark-yellow);
  }
  .back-brand .brand-dot {
    width: 44px;
    height: 44px;
    margin-bottom: 12px;
  }
  .back-brand .brand-name {
    font-size: 19px;
    letter-spacing: 1.5px;
  }
  .contact-block {
    position: absolute;
    right: 60px;
    top: 56px;
    text-align: right;
    color: var(--text-light);
  }
  .company-name {
    font-size: 16px;
    font-weight: 600;
    letter-spacing: 0.4px;
    line-height: 1;
  }
  .person-role {
    margin-top: 9px;
    font-size: 11.5px;
    font-weight: 500;
    line-height: 1.1;
  }
  .person-name {
    font-size: 11.5px;
    font-weight: 500;
    line-height: 1.1;
  }
  .contact-list {
    position: absolute;
    right: 22px;
    top: 124px;
    list-style: none;
    color: var(--text-light);
  }
  .contact-item {
    display: flex;
    align-items: center;
    justify-content: flex-end;
    height: 25px;
    font-size: 12px;
    font-weight: 500;
  }
  .contact-icon {
    width: 16px;
    height: 16px;
    margin-left: 17px;
    flex: none;
  }
  .back-band {
    position: absolute;
    left: 0;
    bottom: 0;
    width: 100%;
    height: 38px;
    border-top: 1px solid rgba(255, 240, 200, 0.35);
    background: linear-gradient(90deg, var(--gold-dark) 0%, var(--gold-mid) 25%, var(--gold-light) 55%, var(--gold-pale) 85%, #ebe0c4 100%);
  }
</style>
</head>
<body>
<main class="presentation">
  <p class="side-label side-label--front">FRONT</p>
  <p class="side-label side-label--back">BACK</p>

  <section class="card card--front" aria-label="Business card front">
    <div class="brand-block">
      <div class="brand-dot"></div>
      <p class="brand-name">KORBALT</p>
      <p class="brand-since">SINCE 2026</p>
    </div>
  </section>

  <section class="card card--back" aria-label="Business card back">
    <div class="back-brand">
      <div class="brand-dot"></div>
      <p class="brand-name">KORBALT</p>
    </div>

    <div class="contact-block">
      <p class="company-name">KORBALT SOLVANG</p>
      <p class="person-role">CEO &amp; FOUNDER</p>
      <p class="person-name">Lars Henrik Solvang</p>
    </div>

    <ul class="contact-list">
      <li class="contact-item">www.korbalt.llc
        <svg class="contact-icon" viewBox="0 0 16 16" fill="none" stroke="var(--icon-light)" stroke-width="1.1">
          <circle cx="8" cy="8" r="6.5"/>
          <ellipse cx="8" cy="8" rx="2.8" ry="6.5"/>
          <line x1="1.5" y1="8" x2="14.5" y2="8"/>
          <path d="M2.6 4.8h10.8M2.6 11.2h10.8"/>
        </svg>
      </li>
      <li class="contact-item">004791586274
        <svg class="contact-icon" viewBox="0 0 16 16" fill="var(--icon-light)">
          <path d="M3.6 1.8l2.2-.3 1.3 3.2-1.5 1.1c.7 1.6 1.9 2.9 3.5 3.6l1.1-1.5 3.2 1.3-.3 2.2c-.1.7-.7 1.2-1.4 1.1C6.5 12 3.9 9.4 3.4 4.2c-.1-.7.4-1.3 1.1-1.4z"/>
        </svg>
      </li>
      <li class="contact-item">korbalt.llc@postmail.com
        <svg class="contact-icon" viewBox="0 0 16 16">
          <rect x="1.5" y="3.5" width="13" height="9" rx="1" fill="var(--icon-light)"/>
          <path d="M2 4.2l6 4.3 6-4.3" fill="none" stroke="var(--gold-mid)" stroke-width="1"/>
        </svg>
      </li>
    </ul>

    <div class="back-band"></div>
  </section>
</main>
</body>
</html>
```